Wordpress Design

Need a responsive wordpress website with the minimum 10 service description pages. This website is for a small business consultancy, providing business development and digital marketing services.

Will also need at least 4 diffrent templates: Home page, service page, Landing Page and blog.

The site will be using block editor.

Coded - Design and coding required

1 page

Sans Serif
• Segoe UI

```html
<!DOCTYPE html>
<html lang="en">
<head>
<meta charset="utf-8">
<title>Brightlens Business Consultancy</title>
<link href="https://fonts.googleapis.com/css2?family=Lato:ital,wght@0,400;0,700;0,900;1,700;1,900&display=swap" rel="stylesheet">
<style>
:root{
  --blue:#1a9be6;
  --ink:#1a1a1a;
  --text:#222;
  --card:#f0f0f0;
  --band:#e6e6e6;
  --grey-btn:#8c8c8c;
  --f-grey:#5a6872;
  --f-teal:#1797ae;
  --f-green:#1fb08a;
  --f-red:#d93a1e;
}
*{box-sizing:border-box;margin:0;padding:0}
html,body{width:1200px;height:2724px;overflow:hidden}
body{font-family:"Lato",sans-serif;color:var(--text);background:#fff;position:relative}
.abs{position:absolute}

/* header */
.site-header{position:absolute;left:0;top:0;width:1200px;height:108px;background:#fff}
.brand{left:76px;top:32px;display:flex;align-items:center;gap:10px}
.brand-dot{width:36px;height:36px;border-radius:50%;border:6px solid var(--blue)}
.brand-name{font-size:28px;font-weight:700;color:var(--ink);line-height:1}
.brand-tag{font-size:10px;letter-spacing:1.5px;color:#777;text-transform:uppercase;margin-top:4px}
.main-nav{left:437px;top:42px;display:flex;gap:38px;font-size:18px;font-weight:700;color:var(--ink)}
.nav-cta{left:990px;top:32px;width:137px;height:45px;border-radius:23px;background:var(--blue);color:#fff;font-size:18px;display:flex;align-items:center;justify-content:center}

/* hero */
.hero{left:0;top:108px;width:1200px;height:608px;background:linear-gradient(90deg,#dde3e7 0%,#d6dde2 45%,#b9a99a 62%,#c9b7a6 78%,#e7e9ea 100%)}
.hero-title{left:76px;top:122px;font-size:50px;font-weight:900;line-height:60px;color:var(--ink)}
.hero-sub{left:77px;top:182px;width:520px;font-size:20px;font-weight:700;line-height:28px;color:#2a2a2a}
.hero-intro{left:74px;top:268px;font-size:31px;font-weight:900;color:var(--ink)}
.hero-intro span{color:var(--blue)}
.hero-body{left:76px;top:318px;width:520px;font-size:20px;font-weight:700;line-height:28px;color:#2a2a2a}
.signup{left:74px;top:425px;width:513px;height:56px;border-radius:28px;background:#fff;box-shadow:0 1px 4px rgba(0,0,0,.15)}
.signup-field{left:24px;top:19px;font-size:16px;color:#333}
.signup-btn{left:358px;top:6px;width:150px;height:44px;border-radius:22px;background:var(--blue);color:#fff;font-size:15px;font-weight:700;display:flex;align-items:center;justify-content:center}
.hero-tag{left:803px;top:559px;width:358px;height:49px;background:#111;border-radius:8px 8px 0 0;color:#fff;font-size:17px;font-weight:700;display:flex;align-items:center;justify-content:center}

/* intro */
.intro{left:165px;top:772px;width:870px;text-align:center;font-size:20px;line-height:33px;color:#2a2a2a}
.intro-accent{left:150px;top:893px;width:900px;text-align:center;font-size:22px;line-height:34px;font-weight:700;color:var(--blue)}

/* service cards */
.service{width:241px;height:210px;border-radius:20px;background:var(--card);text-align:center;font-size:19px;font-weight:700;line-height:28px;color:var(--ink);padding-top:36px}
.service svg{display:block;margin:0 auto 20px}
.service.active{background:var(--blue);color:#fff}

/* funnel */
.funnel-band{left:0;top:1525px;width:1200px;height:470px;background:var(--band)}
.funnel-art{left:75px;top:65px;width:440px;height:350px;border-radius:6px;background:linear-gradient(180deg,#5a6872 0%,#1797ae 35%,#1fb08a 60%,#d93a1e 82%,#f39a1d 100%);opacity:.85}
.funnel-label{font-size:22px;font-weight:700}
.focus-title{left:704px;top:1620px;font-size:37px;font-style:italic;font-weight:900;line-height:44px;color:var(--blue)}
.focus-body{left:704px;top:1718px;width:420px;font-size:19px;line-height:30px;color:#2a2a2a}
.focus-btn{left:704px;top:1845px;width:152px;height:46px;border-radius:23px;background:var(--blue);color:#fff;font-size:19px;display:flex;align-items:center;justify-content:center}

/* call to action */
.cta{left:0;top:1995px;width:1200px;height:367px;background:linear-gradient(120deg,#0b1620 0%,#13273a 55%,#1c3a52 100%)}
.cta-title{left:210px;top:70px;width:780px;text-align:center;font-size:37px;line-height:42px;font-style:italic;font-weight:900;color:#fff}
.cta-sub{left:100px;top:182px;width:1000px;text-align:center;font-size:18px;color:#e8eef3}
.cta-btn{left:411px;top:239px;width:377px;height:46px;border-radius:23px;background:var(--blue);color:#fff;font-size:19px;font-weight:700;display:flex;align-items:center;justify-content:center}

/* contact tiles */
.tile{top:2415px;width:330px;height:100px;border-radius:10px;display:flex;align-items:center;justify-content:center;gap:26px;color:#fff;font-size:24px;font-weight:700;line-height:28px}
.tile.blue{background:var(--blue)}
.tile.dark{background:var(--ink)}
.tile.grey{background:var(--grey-btn)}

/* footer */
.site-footer{left:0;top:2572px;width:1200px;height:152px;background:#e8e8e8}
.footer-nav{left:0;top:24px;width:1200px;display:flex;justify-content:center;gap:36px;font-size:17px;font-weight:700;color:var(--ink)}
.copyright{left:0;top:60px;width:1200px;text-align:center;font-size:15px;color:#222}
.social{left:0;top:93px;width:1200px;display:flex;justify-content:center;gap:24px}
.social span{width:24px;height:24px;border-radius:50%;background:var(--ink)}
</style>
</head>
<body>

<header class="site-header">
  <div class="abs brand">
    <div class="brand-dot"></div>
    <div><div class="brand-name">Brightlens</div><div class="brand-tag">Business Consultancy</div></div>
  </div>
  <nav class="abs main-nav"><span>Business Strategy</span><span>Marketing Strategy</span><span>Blog</span><span>About Us</span></nav>
  <div class="abs nav-cta">Contact Us</div>
</header>

<section class="abs hero" role="img" aria-label="Photo of a smiling consultant at a desk with a laptop and notebook">
  <h1 class="abs hero-title">That feeling you get when</h1>
  <p class="abs hero-sub">You decide to start your own business and realise you need more than 24 hours to get it all done.</p>
  <h2 class="abs hero-intro">Introducing <span>Brightlens</span></h2>
  <p class="abs hero-body">We are here to get you started or just share the load of business optimisation and marketing, so you can concentrate on what you are best at .</p>
  <div class="abs signup">
    <span class="abs signup-field">Enter Email Address</span>
    <span class="abs signup-btn">Get Help Now</span>
  </div>
  <div class="abs hero-tag">Let's get you Closer to our Customers</div>
</section>

<p class="abs intro">At Brightlens, it's never a one size fits all approach. We are a strategy-first consultancy with your customer in mind. Our aim is closely understand your goals, build a clear roadmap, and tackle your highest value projects.</p>
<p class="abs intro-accent">All our efforts are concentrated on reaching your customers where they are -<br>getting you closer to you customers .</p>

<div class="abs service active" style="left:75px;top:1007px">
  <svg width="60" height="60" viewBox="0 0 60 60" fill="none" stroke="#fff" stroke-width="2"><rect x="14" y="6" width="32" height="20" rx="2"/><path d="M8 34h44M12 34v16M48 34v16M22 26v24M38 26v24"/></svg>
  Business Consulting &amp;<br>Advisory</div>
<div class="abs service" style="left:345px;top:1007px">
  <svg width="60" height="60" viewBox="0 0 60 60" fill="none" stroke="var(--blue)" stroke-width="2"><rect x="8" y="8" width="44" height="34"/><path d="M30 42v12M16 18h12M16 26h28M16 34h20"/></svg>
  Business<br>Plan Development</div>
<div class="abs service" style="left:615px;top:1007px">
  <svg width="60" height="60" viewBox="0 0 60 60" fill="none" stroke="var(--blue)" stroke-width="2"><path d="M6 54h48M12 54V40h8v14M26 54V32h8v14M40 54V24h8v30M10 30l14-10 10 6 16-16M42 10h8v8"/></svg>
  Profit and Growth<br>Improvement</div>
<div class="abs service" style="left:885px;top:1007px">
  <svg width="80" height="60" viewBox="0 0 80 60" fill="none" stroke="var(--blue)" stroke-width="2"><rect x="8" y="8" width="64" height="44"/><path d="M8 16h64M2 54h76M26 40l6-14h8v14zM48 26l14-6v20l-14-6z"/></svg>
  Marketing Consulting<br>&amp; Advisory</div>

<div class="abs service" style="left:75px;top:1243px">
  <svg width="60" height="60" viewBox="0 0 60 60" fill="none" stroke="var(--blue)" stroke-width="2"><rect x="6" y="6" width="40" height="30"/><rect x="24" y="28" width="30" height="22"/><path d="M24 28l15 12 15-12M6 14h40"/></svg>
  Brand Building/<br>Strategy</div>
<div class="abs service" style="left:345px;top:1243px">
  <svg width="60" height="60" viewBox="0 0 60 60" fill="none" stroke="var(--blue)" stroke-width="2"><circle cx="30" cy="20" r="14"/><path d="M30 34v8M6 44h48v12H6zM18 44v12M42 44v12"/></svg>
  Customer Experience<br>Mapping</div>
<div class="abs service" style="left:615px;top:1243px">
  <svg width="60" height="60" viewBox="0 0 60 60" fill="none" stroke="var(--blue)" stroke-width="2"><rect x="4" y="8" width="52" height="38"/><path d="M18 54h24M30 46v8M14 18h16v18H14zM36 18h12v10H36z"/></svg>
  Digital Footprint<br>Optimisation</div>
<div class="abs service" style="left:885px;top:1243px">
  <svg width="60" height="60" viewBox="0 0 60 60" fill="none" stroke="var(--blue)" stroke-width="2"><rect x="6" y="6" width="38" height="30"/><path d="M6 14h38M30 30l4 22 6-8 10 10 4-4-10-10 8-6z"/></svg>
  Advertising</div>

<section class="abs funnel-band">
  <div class="abs funnel-art" role="img" aria-label="Sales funnel illustration with stages from awareness down to purchase"></div>
  <span class="abs funnel-label" style="left:527px;top:92px;color:var(--f-grey);font-weight:400">Awareness</span>
  <span class="abs funnel-label" style="left:527px;top:166px;color:var(--f-teal)">Interest</span>
  <span class="abs funnel-label" style="left:527px;top:238px;color:var(--f-green)">Consideration</span>
  <span class="abs funnel-label" style="left:527px;top:313px;color:var(--f-red)">Purchase</span>
</section>
<h2 class="abs focus-title">Focus on what matters<br>the most</h2>
<p class="abs focus-body">Grow your traffic and contribute more pipeline with a suite of services designed to deliver ideal prospects to sales.</p>
<div class="abs focus-btn">Learn More</div>

<section class="abs cta" role="img" aria-label="Dark abstract network background">
  <h2 class="abs cta-title">Ready to transform your business process and marketing efforts?</h2>
  <p class="abs cta-sub">Request a free assessment and get started Request a free 30 min consultation started today</p>
  <div class="abs cta-btn">Request a Free30 min Consulatation</div>
</section>

<div class="abs tile blue" style="left:75px">
  <svg width="44" height="34" viewBox="0 0 44 34"><rect width="44" height="34" rx="4" fill="#fff"/><path d="M3 5l19 14 19-14" fill="none" stroke="var(--blue)" stroke-width="3"/></svg>
  <span>Subscribe to Our<br>Newsletter</span></div>
<div class="abs tile dark" style="left:436px">
  <svg width="36" height="36" viewBox="0 0 24 24"><path fill="#fff" d="M6.6 10.8a15.1 15.1 0 006.6 6.6l2.2-2.2a1 1 0 011-.25 11.4 11.4 0 003.6.57 1 1 0 011 1V20a1 1 0 01-1 1A17 17 0 013 4a1 1 0 011-1h3.5a1 1 0 011 1 11.4 11.4 0 00.57 3.6 1 1 0 01-.25 1z"/></svg>
  <span>Call Now on<br>0400 123 456</span></div>
<div class="abs tile grey" style="left:797px">
  <svg width="44" height="36" viewBox="0 0 44 36"><ellipse cx="18" cy="14" rx="17" ry="12" fill="#fff"/><ellipse cx="30" cy="22" rx="13" ry="10" fill="#fff" stroke="var(--grey-btn)" stroke-width="2"/></svg>
  <span>Contact Us</span></div>

<footer class="abs site-footer">
  <nav class="abs footer-nav"><span>Business Strategy</span><span>Marketing Strategy</span><span>Blog</span><span>About Us</span><span>Contact Us</span></nav>
  <p class="abs copyright">Copyright © 2020 CompanyName All Right Reserved</p>
  <div class="abs social"><span></span><span></span><span></span><span></span><span></span></div>
</footer>

</body>
</html>
```